business card design for a small scale specialty cut flower farm

We need a business card design for Hollowmere Bloom Farm based in Langley, BC, Canada. We produce specialty, high-end cut flowers and sell locally to florists, local shops and markets and the end user through bouquet subscriptions. The final business card design should be memorable and have a timeless or vintage feel. We would prefer a square shape.
Updates

Target Market(s)

florists, shops and seasonal markets, local flower lovers

Industry/Entity Type

Floral

Contact Information for Business Card

Tamsin Ellery Voss, Grower
Langley, BC, Canada
website: hollowmerebloomfarm.example
instagram: @hollowmerebloomfarm
Tel: 555.317.4290
facebook: www.facebook.example/hollowmereblooms/

Font styles to use
Serif
Decorative
Script

Requirements
Must have
• soft black background colour on front side, the included logo and catch phrase: Fresh Local Seasonal
Nice to have
• phone number and website address on front of card, included photo 6539 incorporated onto the back, possibly photo 6609 as well.

```html
<!DOCTYPE html>
<html lang="en">
<head>
<meta charset="utf-8">
<title>Hollowmere Bloom Farm — Business Card</title>
<link href="https://fonts.googleapis.com/css2?family=Lato:wght@400;700&display=swap" rel="stylesheet">
<style>
  :root {
    --page: #ece6d8;
    --soft-black: #1b1a1a;
    --white: #ffffff;
    --rule-green: #3f6b3a;
    --band-green: #4f7a45;
    --band-lime: #b7c748;
    --text-soft: #d9d9d9;
    --foliage: #6fa24a;
    --petal-pink: #e98aa8;
    --wall-pink: #d2456a;
    --bloom-red: #e2364f;
    --bloom-violet: #6a4bc4;
  }
  * { margin: 0; padding: 0; box-sizing: border-box; }
  html, body {
    width: 1200px; height: 960px; overflow: hidden;
    background: var(--page);
    font-family: "Lato", Arial, sans-serif;
  }
  .sheet {
    position: relative; width: 1200px; height: 960px;
    display: flex; flex-direction: column; align-items: center;
    justify-content: center; gap: 40px;
  }
  .card {
    position: relative; width: 700px; height: 400px; overflow: hidden;
    box-shadow: 0 6px 18px rgba(0,0,0,0.18);
  }
  .card-back { background: var(--soft-black); }
  .card-back svg { position: absolute; inset: 0; }

  .card-front { background: var(--soft-black); color: var(--white); }
  .card-front .shapes { position: absolute; inset: 0; }
  .brand {
    position: absolute; left: 50px; top: 150px;
    display: flex; align-items: center; gap: 10px;
  }
  .brand-dot {
    width: 20px; height: 20px; border-radius: 50%;
    background: var(--petal-pink);
  }
  .brand-name {
    font-size: 24px; font-weight: 400; letter-spacing: 0.5px;
    color: var(--white); white-space: nowrap;
  }
  .person {
    position: absolute; right: 60px; top: 60px; text-align: right;
  }
  .person-name { font-size: 26px; font-weight: 700; line-height: 32px; }
  .person-role { font-size: 14px; font-weight: 400; color: var(--text-soft); line-height: 18px; }
  .contact {
    position: absolute; left: 52px; top: 308px;
    font-size: 16px; line-height: 24px; color: var(--white);
  }
  .contact-row { display: flex; align-items: center; gap: 10px; white-space: nowrap; }
  .contact-row svg { width: 14px; height: 14px; flex: none; }
  .tagline {
    position: absolute; right: 34px; top: 348px;
    font-size: 20px; font-weight: 700; color: var(--white); white-space: nowrap;
  }
</style>
</head>
<body>
<main class="sheet">

  <section class="card card-back" aria-label="Card back">
    <svg viewBox="0 0 700 400" width="700" height="400">
      <defs>
        <linearGradient id="gardenTones" x1="0" y1="0" x2="1" y2="1">
          <stop offset="0" stop-color="#dfe8de"/>
          <stop offset="0.35" stop-color="#6fa24a"/>
          <stop offset="0.7" stop-color="#e98aa8"/>
          <stop offset="1" stop-color="#4d7a33"/>
        </linearGradient>
        <linearGradient id="bouquetTones" x1="0" y1="0" x2="0.6" y2="1">
          <stop offset="0" stop-color="#d2456a"/>
          <stop offset="0.3" stop-color="#6a4bc4"/>
          <stop offset="0.55" stop-color="#e2364f"/>
          <stop offset="1" stop-color="#b9d3e6"/>
        </linearGradient>
      </defs>
      <polygon role="img" aria-label="Photo of the grower among pink snapdragons in a green garden"
               points="0,0 330,0 362,400 0,400" fill="url(#gardenTones)"/>
      <polygon role="img" aria-label="Photo of dahlia, hydrangea and delphinium bouquets in metal buckets against a pink wall"
               points="366,0 700,0 700,400 398,400" fill="url(#bouquetTones)"/>
    </svg>
  </section>

  <section class="card card-front" aria-label="Card front">
    <svg class="shapes" viewBox="0 0 700 400" width="700" height="400" aria-hidden="true">
      <line x1="400" y1="126" x2="660" y2="126" stroke="var(--rule-green)" stroke-width="1"/>
      <line x1="50" y1="298" x2="470" y2="298" stroke="var(--rule-green)" stroke-width="1"/>
      <polygon points="0,386 470,358 470,400 0,400" fill="var(--band-lime)"/>
      <polygon points="478,326 700,326 700,400 462,400" fill="var(--band-green)"/>
    </svg>

    <div class="brand">
      <span class="brand-dot"></span>
      <span class="brand-name">Hollowmere Bloom Farm</span>
    </div>

    <div class="person">
      <div class="person-name">Tamsin Ellery Voss</div>
      <div class="person-role">Owner</div>
    </div>

    <div class="contact">
      <div class="contact-row">
        <svg viewBox="0 0 14 14" aria-hidden="true">
          <path d="M3 1.5 L5 1.5 L6 4.5 L4.6 5.6 C5.4 7.3 6.7 8.6 8.4 9.4 L9.5 8 L12.5 9 L12.5 11 C12.5 12 11.7 12.6 10.8 12.5 C5.8 12 2 8.2 1.5 3.2 C1.4 2.3 2 1.5 3 1.5 Z" fill="var(--band-lime)"/>
        </svg>
        <span>(555) 317-4290</span>
      </div>
      <div class="contact-row">
        <svg viewBox="0 0 14 14" aria-hidden="true">
          <circle cx="7" cy="7" r="5.8" fill="none" stroke="var(--band-lime)" stroke-width="1.3"/>
          <ellipse cx="7" cy="7" rx="2.5" ry="5.8" fill="none" stroke="var(--band-lime)" stroke-width="1"/>
          <line x1="1.2" y1="7" x2="12.8" y2="7" stroke="var(--band-lime)" stroke-width="1"/>
        </svg>
        <span>www.hollowmerebloomfarm.example</span>
      </div>
    </div>

    <div class="tagline">Fresh Local Seasonal</div>
  </section>

</main>
</body>
</html>
```